Business Card Design

new real estate company in the Colorado mountains would like fun..creative.. pines trees and house and dog(s)? heart? I love colors

I am also asking for a logo design then to biz cards..

Industry/Entity Type

Real Estate

Contact Information for Business Card

Meadowlark Bend Realty

Rosalind Tavers
"Your Go-To-Gal for Real Estate!"
555-316-0847
rosalindmtavers@brightpost.example

```html
<!DOCTYPE html>
<html lang="en">
<head>
<meta charset="utf-8">
<title>Meadowlark Bend Realty — Business Card</title>
<link rel="stylesheet" href="https://fonts.googleapis.com/css2?family=Open+Sans:wght@400;600;700&display=swap">
<style>
  :root {
    --stage: #2a2a2c;
    --card: #eeeff1;
    --card-edge: #dcdde0;
    --navy: #0f2d63;
    --sky: #29a8e0;
    --ink: #4a4a4a;
    --white: #ffffff;
  }
  * { box-sizing: border-box; margin: 0; padding: 0; }
  html, body { width: 1200px; height: 908px; overflow: hidden; }
  body {
    background: var(--stage);
    font-family: "Open Sans", Arial, sans-serif;
    position: relative;
  }
  .card {
    position: absolute;
    width: 640px;
    height: 366px;
    border-radius: 26px;
    background: linear-gradient(135deg, var(--white) 0%, var(--card) 60%, var(--card-edge) 100%);
    overflow: hidden;
    box-shadow: 0 14px 34px rgba(0,0,0,.45);
  }
  .card--logo { left: 110px; top: 70px; }
  .card--contact { left: 450px; top: 470px; }

  .brand {
    position: absolute;
    display: flex;
    align-items: center;
    gap: 12px;
  }
  .card--logo .brand { left: 170px; top: 160px; }
  .card--contact .brand { right: 34px; top: 212px; }
  .brand__dot {
    width: 34px; height: 34px; border-radius: 50%;
    background: var(--sky);
    flex: none;
  }
  .card--contact .brand__dot { width: 30px; height: 30px; }
  .brand__name {
    font-weight: 700;
    font-size: 22px;
    color: var(--navy);
    letter-spacing: 1px;
    white-space: nowrap;
  }
  .card--contact .brand__name { font-size: 17px; letter-spacing: .8px; }

  .wave { position: absolute; inset: 0; width: 100%; height: 100%; }

  .contact {
    position: absolute;
    left: 22px; top: 30px;
    list-style: none;
    color: var(--white);
    font-size: 12.5px;
    line-height: 19px;
  }
  .contact li { display: flex; align-items: flex-start; gap: 7px; }
  .contact svg { flex: none; margin-top: 3px; }

  .person { position: absolute; left: 26px; bottom: 26px; }
  .person__name { color: var(--sky); font-weight: 700; font-size: 22px; line-height: 28px; }
  .person__title { color: var(--ink); font-weight: 400; font-size: 19px; line-height: 24px; }
</style>
</head>
<body>

  <section class="card card--logo" aria-label="Card back">
    <div class="brand">
      <span class="brand__dot"></span>
      <span class="brand__name">Meadowlark Bend Realty</span>
    </div>
  </section>

  <section class="card card--contact" aria-label="Card front">
    <svg class="wave" viewBox="0 0 640 366" preserveAspectRatio="none" aria-hidden="true">
      <path d="M0,0 H640 V18 C520,40 410,80 300,140 C210,190 110,215 0,220 Z" fill="var(--navy)"/>
      <path d="M0,234 C120,228 220,200 320,150 C430,95 530,55 640,34" fill="none" stroke="var(--navy)" stroke-width="7"/>
      <path d="M0,252 C130,246 240,215 340,165 C450,110 540,75 640,56" fill="none" stroke="var(--sky)" stroke-width="9"/>
    </svg>

    <ul class="contact">
      <li><svg width="10" height="10" viewBox="0 0 10 10"><circle cx="5" cy="5" r="5" fill="#fff"/><path d="M5 2a2 2 0 0 0-2 2c0 1.5 2 4 2 4s2-2.5 2-4a2 2 0 0 0-2-2z" fill="var(--navy)"/></svg><span>Suite # 118, Ridge Bldg,<br>CO 80517</span></li>
      <li><svg width="10" height="10" viewBox="0 0 10 10"><circle cx="5" cy="5" r="5" fill="#fff"/><rect x="3.5" y="2" width="3" height="6" rx="1" fill="var(--navy)"/></svg><span>555-316-0847</span></li>
      <li><svg width="10" height="10" viewBox="0 0 10 10"><circle cx="5" cy="5" r="5" fill="#fff"/><rect x="3.5" y="2" width="3" height="6" rx="1" fill="var(--navy)"/></svg><span>555-208-4419</span></li>
      <li><svg width="10" height="10" viewBox="0 0 10 10"><circle cx="5" cy="5" r="5" fill="#fff"/><rect x="2.5" y="3" width="5" height="4" fill="var(--navy)"/></svg><span>555-730-6652</span></li>
      <li><svg width="10" height="10" viewBox="0 0 10 10"><circle cx="5" cy="5" r="5" fill="#fff"/><rect x="2.5" y="3" width="5" height="4" fill="none" stroke="var(--navy)"/><path d="M2.5 3l2.5 2 2.5-2" fill="none" stroke="var(--navy)" stroke-width=".8"/></svg><span>rosalindmtavers@brightpost.example</span></li>
      <li><svg width="10" height="10" viewBox="0 0 10 10"><circle cx="5" cy="5" r="5" fill="#fff"/><circle cx="5" cy="5" r="2.8" fill="none" stroke="var(--navy)" stroke-width=".8"/><path d="M2.2 5h5.6M5 2.2v5.6" stroke="var(--navy)" stroke-width=".7"/></svg><span>www.meadowlarkbend.example</span></li>
    </ul>

    <div class="brand">
      <span class="brand__dot"></span>
      <span class="brand__name">Meadowlark Bend Realty</span>
    </div>

    <div class="person">
      <p class="person__name">Rosalind Tavers</p>
      <p class="person__title">Owner / C.E.O</p>
    </div>
  </section>

</body>
</html>
```